Law Office business card design

I have a general practice specializing in criminal defense work and domestic cases. I have extensive trial and appellate experience.

Target Market(s)

general public

Industry/Entity Type

Defense

Contact Information for Business Card

Darrowby Law Office, P.A.
382 N. 4th
PO Box 5274
Ashgrove, OK 67409-5274
(555) 555-0172
(555) 555-0198 FAX
tdarrow@plinkmail.example

Requirements
Must have
• A symbol that immediately identifes the card as a legal practice.

```html
<!DOCTYPE html>
<html lang="en">
<head>
<meta charset="utf-8">
<title>Darrowby Law Office – Business Card</title>
<link rel="stylesheet" href="https://fonts.googleapis.com/css2?family=Josefin+Sans:wght@300;400&display=swap">
<style>
  :root {
    --stage: #8e8e8e;
    --stage-dark: #3a3a3a;
    --panel-deep: #5e120f;
    --panel: #7d1a16;
    --bar: #a3231f;
    --bar-light: #b52b26;
    --photo-dark: #5a1a0c;
    --photo-mid: #c4531c;
    --photo-warm: #e07a2c;
    --photo-gold: #e6bb6c;
    --ink: #ffffff;
    --divider: #ffffff;
  }
  * { margin: 0; padding: 0; box-sizing: border-box; }
  html, body { width: 1200px; height: 900px; overflow: hidden; }
  body {
    background: radial-gradient(ellipse at 50% 45%, var(--stage) 0%, var(--stage-dark) 100%);
    font-family: "Josefin Sans", "Century Gothic", sans-serif;
    color: var(--ink);
    position: relative;
  }
  .card {
    position: absolute;
    left: 150px; top: 193px;
    width: 900px; height: 514px;
    overflow: hidden;
    box-shadow: 0 18px 40px rgba(0,0,0,.45);
  }
  .card__photo {
    position: absolute; inset: 0;
    background:
      radial-gradient(ellipse at 68% 38%, var(--photo-gold) 0%, rgba(230,187,108,0) 38%),
      radial-gradient(ellipse at 78% 78%, rgba(230,187,108,.75) 0%, rgba(230,187,108,0) 35%),
      linear-gradient(120deg, var(--photo-dark) 0%, var(--photo-mid) 45%, var(--photo-warm) 70%, var(--photo-mid) 100%);
  }
  .card__panel {
    position: absolute; inset: 0;
    clip-path: polygon(0 0, 300px 0, 720px 514px, 0 514px);
    background:
      radial-gradient(ellipse at 35% 70%, rgba(40,6,4,.55) 0%, rgba(40,6,4,0) 45%),
      linear-gradient(160deg, var(--panel) 0%, var(--panel-deep) 100%);
  }
  .card__divider { position: absolute; inset: 0; }
  .brand {
    position: absolute; left: 62px; top: 74px;
    text-transform: uppercase; font-weight: 300;
  }
  .brand__name { font-size: 44px; letter-spacing: 1px; line-height: 1; }
  .brand__sub { font-size: 26px; letter-spacing: 4px; line-height: 1; margin: 4px 0 0 22px; }
  .contacts { position: absolute; left: 150px; top: 200px; list-style: none; }
  .contact { display: flex; align-items: center; height: 36px; margin-bottom: 10px; }
  .contact__icon {
    width: 36px; height: 36px; background: var(--bar);
    display: flex; align-items: center; justify-content: center; margin-right: 6px;
  }
  .contact__text {
    height: 36px; width: 520px; padding-left: 14px;
    background: linear-gradient(90deg, var(--bar-light), var(--bar));
    font-size: 19px; letter-spacing: 2px; line-height: 38px; font-weight: 400;
  }
  .address {
    position: absolute; left: 62px; top: 445px;
    font-size: 14px; letter-spacing: 1.2px; text-transform: uppercase; font-weight: 400;
  }
</style>
</head>
<body>
  <div class="card">
    <div class="card__photo" role="img" aria-label="Warm close-up photograph of brass scales of justice on a wooden desk"></div>
    <div class="card__panel" role="img" aria-label="Dark red tinted photograph of a judge's gavel">
      <div class="brand">
        <div class="brand__name">Darrowby</div>
        <div class="brand__sub">Law Office</div>
      </div>
      <ul class="contacts">
        <li class="contact">
          <span class="contact__icon"><svg width="14" height="22" viewBox="0 0 14 22"><rect x="1" y="1" width="12" height="20" rx="2" fill="none" stroke="#fff" stroke-width="2"/><rect x="3.5" y="4" width="7" height="8" fill="#fff"/><circle cx="7" cy="17" r="1.5" fill="#fff"/></svg></span>
          <span class="contact__text">(555) 555-0172</span>
        </li>
        <li class="contact">
          <span class="contact__icon"><svg width="22" height="20" viewBox="0 0 22 20"><rect x="5" y="1" width="12" height="7" fill="none" stroke="#fff" stroke-width="1.8"/><rect x="1" y="8" width="20" height="11" rx="1.5" fill="#fff"/><rect x="5" y="11" width="12" height="2" fill="#a3231f"/><rect x="5" y="15" width="8" height="2" fill="#a3231f"/></svg></span>
          <span class="contact__text">(555) 555-0198</span>
        </li>
        <li class="contact">
          <span class="contact__icon"><svg width="22" height="16" viewBox="0 0 22 16"><rect x="0" y="0" width="22" height="16" fill="#fff"/><path d="M0 0 L11 9 L22 0" fill="none" stroke="#a3231f" stroke-width="1.8"/></svg></span>
          <span class="contact__text">tdarrow@plinkmail.example</span>
        </li>
      </ul>
      <p class="address">P.A. 382 N. 4th PO Box 5274 Ashgrove, OK 67409-5274</p>
    </div>
    <svg class="card__divider" width="900" height="514" viewBox="0 0 900 514" aria-hidden="true">
      <line x1="300" y1="-2" x2="722" y2="516" stroke="var(--divider)" stroke-width="5"/>
    </svg>
  </div>
</body>
</html>
```